Amber Ridge Publishing Web Page Design

Design a website for my new start up publishing company - Amber Ridge Publishing, the first work published by ARP with be a new book by M.R. Theodor called Silent Ledger. The prototype for the book cover is attached.

Target Market(s)

Worldwide, all readers of mystery, fiction, etc.

Industry/Entity Type

Book Publisher

Coding

Coded - Design and coding required

Number of Pages Required

1 page

```html
<!DOCTYPE html>
<html lang="en">
<head>
<meta charset="utf-8">
<title>Amber Ridge Publishing</title>
<link href="https://fonts.googleapis.com/css2?family=Poppins:wght@300;400;500;600;700&display=swap" rel="stylesheet">
<style>
:root{
  --purple:#6a4cf4;
  --purple-soft:#ece8ff;
  --ink:#23232f;
  --muted:#8a8a99;
  --line:#e3e3ea;
  --white:#ffffff;
  --footer:#1d1d27;
}
*{box-sizing:border-box;margin:0;padding:0}
html,body{width:1200px;height:2688px;overflow:hidden;background:var(--white)}
body{font-family:'Poppins',sans-serif;color:var(--ink);position:relative}
.canvas{position:relative;width:1200px;height:2688px;overflow:hidden}
.abs{position:absolute}
.waves{position:absolute;left:0;top:0}

/* header */
.brand{left:224px;top:8px;display:flex;align-items:center;gap:8px;z-index:2;background:var(--white);padding:4px 8px 4px 0}
.brand-mark{width:12px;height:12px;background:var(--purple)}
.brand-name{font-size:15px;font-weight:500;line-height:1.1;color:var(--ink);width:120px}
.nav{left:540px;top:24px;display:flex;gap:20px;font-size:9.5px;font-weight:500;letter-spacing:.5px;color:var(--ink);white-space:nowrap}
.nav .active{color:var(--purple)}
.search{left:944px;top:20px}

/* hero */
.hero-photo{left:248px;top:62px;width:210px;height:276px;background:linear-gradient(180deg,#f1ece8,#d9c7bc 60%,#b9876e)}
.hero-title{left:620px;top:104px;font-size:30px;font-weight:400;line-height:1.15;color:var(--ink)}
.hero-title strong{color:var(--purple);font-weight:600}
.hero-kicker{left:622px;top:216px;font-size:10px;letter-spacing:2px;color:var(--muted);font-weight:500}

/* about card */
.about-card{left:236px;top:376px;width:728px;height:420px;background:var(--white);box-shadow:0 20px 50px rgba(40,20,120,.12)}
.eyebrow{font-size:10px;font-weight:600;letter-spacing:1.6px;color:var(--muted);text-transform:uppercase}
.about-left{left:36px;top:40px;width:300px}
.about-title{margin-top:18px;font-size:30px;font-weight:300;line-height:1.2}
.about-title strong{color:var(--purple);font-weight:600}
.about-photo{left:30px;top:230px;width:300px;height:150px;background:linear-gradient(160deg,#f7f7f8,#e4e4e8 55%,#cfcfd6)}
.about-right{left:372px;top:40px;width:320px;font-size:11px;line-height:1.8;color:var(--muted)}
.about-right p{margin-top:14px}
.quote{margin-top:22px;padding:14px 16px;border-left:4px solid var(--purple);background:var(--purple-soft);color:var(--ink);font-size:11px;line-height:1.7}

/* services */
.services-title{left:0;top:844px;width:1200px;text-align:center;font-size:30px;font-weight:300;color:var(--white)}
.service{top:930px;width:200px;text-align:center;color:var(--white)}
.service h3{font-size:13px;font-weight:600;margin-top:14px}
.service p{font-size:10px;line-height:1.7;margin-top:8px;opacity:.85}
.releases-eyebrow{left:0;top:1190px;width:1200px;text-align:center;color:#d8d0ff}
.releases-title{left:0;top:1212px;width:1200px;text-align:center;font-size:30px;font-weight:300;color:var(--white)}

/* book */
.book-cover{left:316px;top:1452px;width:138px;height:204px;background:linear-gradient(160deg,#2f3a8c,#141a4a 60%,#0a0d24);box-shadow:12px 14px 26px rgba(0,0,0,.3)}
.book-info{left:616px;top:1508px;width:340px}
.book-title{font-size:36px;font-weight:400;color:var(--purple);margin-top:6px}
.book-text{font-size:11px;line-height:1.8;color:var(--muted);margin-top:12px}

/* newsletter */
.news{left:236px;top:1990px;width:380px}
.news-title{font-size:32px;font-weight:300;line-height:1.2;margin-top:10px}
.news-title strong{color:var(--purple);font-weight:600}
.news-text{font-size:11px;line-height:1.8;color:var(--muted);margin-top:14px}
.field{border:1px solid var(--line);height:34px;font-size:10px;color:var(--muted);padding:0 12px;display:flex;align-items:center;background:var(--white)}
.news .field{margin-top:18px;width:360px}
.btn{display:inline-flex;align-items:center;justify-content:center;height:30px;padding:0 18px;font-size:10px;font-weight:600;letter-spacing:1px;background:var(--purple);color:var(--white);margin-top:12px}
.author-photo{left:716px;top:1850px;width:280px;height:330px;background:linear-gradient(180deg,#eef0f3,#c9cdd6 55%,#8e99ad)}

/* contact */
.contact{left:236px;top:2278px;width:340px}
.contact-title{font-size:30px;font-weight:600;margin-top:8px}
.contact-lines{margin-top:22px;font-size:11px;line-height:1.95;color:var(--muted)}
.contact-lines b{color:var(--ink);font-weight:600}
.socials{display:flex;gap:14px;margin-top:20px}
.socials span{width:12px;height:12px;border-radius:50%;background:#c9c9d4}
.contact-form{left:640px;top:2282px;width:320px}
.contact-form .field{margin-bottom:12px}
.contact-form .area{height:96px;align-items:flex-start;padding-top:10px}
.btn-outline{background:var(--white);color:var(--ink);border:1px solid var(--line);margin-top:4px}

/* footer */
.footer{left:0;top:2640px;width:1200px;height:48px;background:var(--footer)}
.footer-nav{position:absolute;left:300px;top:18px;display:flex;gap:22px;font-size:9.5px;font-weight:500;color:var(--white);letter-spacing:.5px;white-space:nowrap}
.footer-copy{position:absolute;right:236px;top:19px;font-size:9px;color:#8c8ca0;white-space:nowrap}
</style>
</head>
<body>
<div class="canvas">

  <svg class="waves" width="1200" height="2688" viewBox="0 0 1200 2688" aria-hidden="true">
    <path d="M0 340 C350 300 600 262 850 242 C1000 230 1120 192 1200 172 L1200 1340 C1000 1420 700 1345 500 1385 C300 1420 120 1372 0 1342 Z" fill="#6a4cf4"/>
    <path d="M0 1450 C200 1420 300 1500 500 1470 L500 1480 C300 1520 200 1440 0 1480 Z" fill="#ece8ff"/>
    <path d="M640 1690 C800 1640 1000 1700 1200 1640 L1200 1660 C1000 1720 800 1665 640 1705 Z" fill="#ece8ff"/>
    <path d="M0 1870 C300 1905 600 1810 900 1788 C1050 1776 1150 1746 1200 1726 L1200 1812 C1000 1840 700 1885 400 1922 C200 1946 80 1932 0 1922 Z" fill="#6a4cf4"/>
    <path d="M560 2262 C780 2182 1000 2204 1200 2122 L1200 2208 C1000 2262 800 2252 560 2272 Z" fill="#6a4cf4"/>
  </svg>

  <header>
    <div class="abs brand"><span class="brand-mark"></span><span class="brand-name">Amber Ridge Publishing</span></div>
    <nav class="abs nav">
      <span class="active">HOME</span><span>ABOUT US</span><span>OUR SERVICES</span><span>BOOKS</span><span>NEWS</span><span>CONTACT US</span>
    </nav>
    <svg class="abs search" width="14" height="14" viewBox="0 0 14 14" aria-hidden="true"><circle cx="6" cy="6" r="4.5" fill="none" stroke="#23232f" stroke-width="1.6"/><line x1="9.3" y1="9.3" x2="13" y2="13" stroke="#23232f" stroke-width="1.6"/></svg>
  </header>

  <section class="hero">
    <div class="abs hero-photo" role="img" aria-label="Smiling young man in a sweater, hero portrait"></div>
    <h1 class="abs hero-title">Making Your<br>Creative Ideas<br><strong>Come True</strong></h1>
    <div class="abs hero-kicker">DISCOVER YOUR NEXT BOOK</div>
  </section>

  <section class="abs about-card">
    <div class="abs about-left">
      <div class="eyebrow">Welcome to our house</div>
      <h2 class="about-title">Your Succeeded<br><strong>Book Publishing</strong><br>Is Our Duty</h2>
    </div>
    <div class="abs about-photo" role="img" aria-label="Desk with coffee cup, notebook and glasses"></div>
    <div class="abs about-right">
      <div class="eyebrow">Learn more about us</div>
      <p>We publish stories that stay with readers long after the last page is turned and the lights go out.</p>
      <p>Our editors work closely with every author, from first draft to final print, across every market.</p>
      <div class="quote">Our dedicated team of publishing professionals is committed to helping authors bring their work to readers everywhere, with care and craft.</div>
    </div>
  </section>

  <section class="services">
    <h2 class="abs services-title">Our Services</h2>
    <div class="abs service" style="left:248px">
      <svg width="34" height="30" viewBox="0 0 34 30" aria-hidden="true"><rect x="4" y="3" width="26" height="24" rx="2" fill="none" stroke="#fff" stroke-width="2"/><line x1="17" y1="3" x2="17" y2="27" stroke="#fff" stroke-width="2"/></svg>
      <h3>Books Design</h3>
      <p>Covers and layouts shaped around the story you want to tell.</p>
    </div>
    <div class="abs service" style="left:500px">
      <svg width="34" height="30" viewBox="0 0 34 30" aria-hidden="true"><rect x="6" y="4" width="22" height="22" fill="none" stroke="#fff" stroke-width="2"/><line x1="11" y1="11" x2="23" y2="11" stroke="#fff" stroke-width="2"/><line x1="11" y1="17" x2="23" y2="17" stroke="#fff" stroke-width="2"/></svg>
      <h3>Books Publishing</h3>
      <p>Careful editing, printing and release in print and digital form.</p>
    </div>
    <div class="abs service" style="left:752px">
      <svg width="34" height="30" viewBox="0 0 34 30" aria-hidden="true"><path d="M5 12 L22 5 L22 25 L5 18 Z" fill="none" stroke="#fff" stroke-width="2"/><line x1="26" y1="15" x2="31" y2="15" stroke="#fff" stroke-width="2"/></svg>
      <h3>Books Marketing</h3>
      <p>Campaigns that bring your book in front of the right readers.</p>
    </div>
    <div class="abs eyebrow releases-eyebrow">Browse our new books</div>
    <h2 class="abs releases-title">Latest Books Releases</h2>
  </section>

  <section class="book">
    <div class="abs book-cover" role="img" aria-label="Cover of the novel Silent Ledger, dark blue with lightning over a city"></div>
    <div class="abs book-info">
      <div class="eyebrow">New book by M.R. Theodor</div>
      <h2 class="book-title">Silent Ledger</h2>
      <p class="book-text">A quiet accountant finds one entry that should not exist, and the numbers begin to tell a story nobody wanted heard.</p>
    </div>
  </section>

  <section class="newsletter">
    <div class="abs author-photo" role="img" aria-label="Portrait of a man in a shirt and tie, hand on chin"></div>
    <div class="abs news">
      <div class="eyebrow">Subscribe to newsletter</div>
      <h2 class="news-title">Get the <strong>Latest News</strong><br>of our Authors</h2>
      <p class="news-text">Sign up to hear about new releases, author interviews and events from our growing list.</p>
      <div class="field">Your Email</div>
      <span class="btn">SUBSCRIBE</span>
    </div>
  </section>

  <section class="contact-section">
    <div class="abs contact">
      <div class="eyebrow">Get in touch</div>
      <h2 class="contact-title">Contact Details</h2>
      <div class="contact-lines">
        <b>Phone:</b> +1 555 0148 236<br>
        <b>Email:</b> hello@amberridge.example<br>
        <b>Address:</b> 24 Orchard Lane, Fairbrook, NY 10020<br>
        <b>Opening Hours:</b><br>
        Monday – Thursday 9:00 – 18:00<br>
        Friday – Sunday 10:00 – 16:00
      </div>
      <div class="socials"><span></span><span></span><span></span><span></span><span></span></div>
    </div>
    <form class="abs contact-form">
      <div class="field">Your Name</div>
      <div class="field">Email Address</div>
      <div class="field">Subject</div>
      <div class="field area">Your Message</div>
      <span class="btn btn-outline">SEND MESSAGE</span>
    </form>
  </section>

  <footer class="abs footer">
    <div class="footer-nav"><span>HOME</span><span>ABOUT US</span><span>OUR SERVICES</span><span>BOOKS</span><span>NEWS</span><span>CONTACT US</span></div>
    <div class="footer-copy">© 2024 Amber Ridge Publishing. All rights reserved.</div>
  </footer>

</div>
</body>
</html>
```